prestige web design for KELVA Finance

Hi Guys,

Looking to team up with a creative designer for another of our websites for KELVA finance.
if looking for our similar website www.brimlendco.com.au is one of our other companies. ideally working in our logo being black and white.

Please see attachments for our logo and a description
HOME
VEHICLE
EQUIPMENT
WHO WE ARE
CONTACT US

open to ideas on layout .

touch base if you have any questions.

Target Market(s)

Prestige cars and equipment -trucks earthmoving

Industry/Entity Type

finance

Coding

Coded - Design and coding required

Number of Pages Required

5+ page

Font styles to use
Sans Serif

Colors

Designer to choose colors to be used in the design.

```html
<!DOCTYPE html>
<html lang="en">
<head>
<meta charset="utf-8">
<title>KELVA Finance</title>
<link href="https://fonts.googleapis.com/css2?family=Archivo:wght@700;800;900&family=Poppins:wght@300;400;500;600&display=swap" rel="stylesheet">
<style>
:root{
  --ink:#0b0b0b;
  --night:#06141c;
  --night-2:#0f2a36;
  --mist:#eeeeee;
  --line:#3a3a3a;
  --muted:#555555;
  --ghost:#e4e4e4;
  --white:#ffffff;
}
*{margin:0;padding:0;box-sizing:border-box}
html,body{width:1200px;height:3735px;overflow:hidden;background:var(--white)}
body{position:relative;font-family:"Poppins",sans-serif;color:var(--ink)}
.abs{position:absolute}
.brand{font-family:"Archivo",sans-serif;font-weight:800;font-size:34px;letter-spacing:1px;color:var(--ink)}
.nav{top:38px;left:567px;display:flex;gap:23px;font-size:12.5px}
.nav a{color:var(--ink);text-decoration:none;position:relative}
.nav a.active::after{content:"";position:absolute;left:0;right:0;bottom:-10px;height:2px;background:var(--ink)}
.phone-pill{left:961px;top:25px;width:260px;height:43px;background:var(--ink);border-radius:22px 0 0 22px;color:var(--white);display:flex;align-items:center;gap:12px;padding-left:14px;font-family:"Archivo",sans-serif;font-weight:700;font-size:17px}
.hero-title{left:61px;top:152px;font-family:"Archivo",sans-serif;font-weight:900;line-height:1}
.hero-title .big{font-size:56px;letter-spacing:2px}
.hero-title .sub{font-size:48px;font-weight:800;margin-top:6px;display:block}
.hero-copy{left:62px;top:273px;font-size:12.5px;line-height:21px;color:#222;width:410px}
.pill-btn{display:flex;align-items:center;justify-content:space-between;border:1.5px solid var(--ink);border-radius:26px;background:var(--white);font-family:"Archivo",sans-serif;font-weight:700;font-size:15px;color:var(--ink);padding:0 14px 0 21px;text-decoration:none}
.ghost{font-family:"Archivo",sans-serif;font-weight:700;font-size:150px;line-height:1;color:transparent;-webkit-text-stroke:1.5px var(--ghost);white-space:nowrap}
.photo{position:absolute}
.sec-title{font-family:"Archivo",sans-serif;font-weight:800;font-size:35px;color:var(--ink)}
.sec-copy{font-size:11.5px;line-height:21px;color:var(--muted);width:410px}
.sec-copy p+p{margin-top:11px}
.rule{height:1.5px;background:var(--line)}
.contact-head{left:0;width:1200px;text-align:center}
.field{left:355px;width:489px;border-bottom:1.5px solid var(--line);font-size:11px;color:#555;padding-left:4px}
.footer-col h4{font-family:"Poppins",sans-serif;font-weight:600;font-size:17px;color:var(--white);margin-bottom:16px}
.footer-col li{list-style:none;font-size:11px;color:#ddd;margin-bottom:10px}
.foot-info{font-size:12px;color:#ddd}
</style>
</head>
<body>

<!-- Header -->
<div class="abs brand" style="left:60px;top:18px">KELVA Finance</div>
<nav class="abs nav">
  <a class="active" href="#">Home</a><a href="#">Vehicle</a><a href="#">Equipment</a><a href="#">Who We Are</a><a href="#">Contact Us</a>
</nav>
<div class="abs phone-pill">
  <svg width="26" height="26" viewBox="0 0 24 24" fill="none" stroke="#fff" stroke-width="1.8"><path d="M5 3h4l2 5-2.5 1.5a11 11 0 0 0 6 6L16 13l5 2v4a2 2 0 0 1-2 2A16 16 0 0 1 3 5a2 2 0 0 1 2-2z"/></svg>
  123 98 76540
</div>

<!-- Hero -->
<svg class="abs" style="left:0;top:140px" width="1200" height="580" viewBox="0 0 1200 580">
  <defs>
    <linearGradient id="heroNight" x1="0" y1="0" x2="0" y2="1">
      <stop offset="0" stop-color="#14323f"/><stop offset="1" stop-color="#03090d"/>
    </linearGradient>
  </defs>
  <path d="M0 60 C150 30 300 150 480 150 C700 150 820 10 1000 10 C1100 10 1160 20 1200 10 L1200 420 L0 420 Z" fill="var(--mist)"/>
  <path d="M0 195 C120 150 240 240 420 240 C560 240 600 180 700 180 C820 180 900 220 1050 190 C1120 178 1170 170 1200 160 L1200 420 L690 575 L0 410 Z" fill="url(#heroNight)" role="img" aria-label="Red car driving up rising stacks of coins over a dark finance chart"/>
  <rect x="683" y="528" width="16" height="26" rx="8" fill="none" stroke="#fff" stroke-width="1.5"/>
  <line x1="691" y1="534" x2="691" y2="540" stroke="#fff" stroke-width="1.5"/>
</svg>
<div class="photo" style="left:640px;top:200px;width:400px;height:370px;border-radius:30px;background:radial-gradient(ellipse at 55% 30%,#c8202a 0,#8a1c20 22%,#6b5a45 45%,rgba(60,52,40,.6) 65%,rgba(0,0,0,0) 80%)" role="img" aria-label="Red SUV on stacked coins"></div>
<div class="abs hero-title"><span class="big">KELVA</span><span class="sub">VEHICAL FINANCE</span></div>
<p class="abs hero-copy">Lorem Ipsum has been the industry's standard dummy text ever since the, when an unknown printer took</p>
<a class="abs pill-btn" href="#" style="left:61px;top:335px;width:178px;height:42px">CONTACT US
  <svg width="38" height="26" viewBox="0 0 38 26" fill="none" stroke="#111" stroke-width="1.3"><circle cx="25" cy="13" r="11"/><path d="M2 13h30M26 7l6 6-6 6"/></svg></a>

<!-- Vehicle -->
<div class="abs ghost" style="left:536px;top:770px">VEHICLE</div>
<div class="photo" style="left:0;top:988px;width:449px;height:287px;background:linear-gradient(160deg,#8e9aa3,#c9cdd0 45%,#4d5459)" role="img" aria-label="Silver luxury car parked by the sea at sunset"></div>
<div class="photo" style="left:313px;top:865px;width:367px;height:170px;background:linear-gradient(120deg,#e3e5e6,#d7a24a 55%,#ececec)" role="img" aria-label="Hand using a calculator beside a small red toy car"></div>
<h2 class="abs sec-title" style="left:555px;top:1075px">VEHICLE</h2>
<div class="abs sec-copy" style="left:558px;top:1128px">
  <p>Lorem Ipsum has been the industry's standard dummy text ever since the 1500s, when an unknown printer took a galley of type &amp; scrambled it to make a type specimen book.</p>
  <p>Lorem Ipsum has been the industry's standard dummy text ever since the 1500s, when an unknown printer took a galley of type  scrambled it to make a type specimen book. Lorem Ipsum has been the industry's standard dummy text ever since the, when an unknown.</p>
</div>
<div class="abs rule" style="left:0;top:1353px;width:560px"></div>
<a class="abs pill-btn" href="#" style="left:558px;top:1331px;width:187px;height:45px">LEARN MORE
  <svg width="38" height="26" viewBox="0 0 38 26" fill="none" stroke="#111" stroke-width="1.3"><circle cx="25" cy="13" r="11"/><path d="M2 13h30M26 7l6 6-6 6"/></svg></a>

<!-- Equipment -->
<div class="abs ghost" style="left:0;top:1455px">EQUIPMENT</div>
<svg class="abs" style="left:541px;top:1475px" width="659" height="644" viewBox="0 0 659 644">
  <defs>
    <linearGradient id="dusk" x1="0" y1="0" x2="0" y2="1">
      <stop offset="0" stop-color="#4d6c8a"/><stop offset=".3" stop-color="#e0a256"/><stop offset=".5" stop-color="#7d6a4e"/><stop offset="1" stop-color="#3f3a33"/>
    </linearGradient>
  </defs>
  <polygon points="0,58 659,0 659,644 0,583" fill="url(#dusk)" role="img" aria-label="Yellow wheel loader on a gravel site under a sunset sky"/>
</svg>
<div class="abs" style="left:150px;top:1595px;width:499px;height:391px;background:var(--white)"></div>
<h2 class="abs sec-title" style="left:184px;top:1651px">EQUIPMENT</h2>
<div class="abs sec-copy" style="left:185px;top:1708px">
  <p>Lorem Ipsum has been the industry's standard dummy text ever since the 1500s, when an unknown printer took a galley of type &amp; scrambled it to make a type specimen book.</p>
  <p>Lorem Ipsum has been the industry's standard dummy text ever since the 1500s, when an unknown printer took a galley of type  scrambled it to make a type specimen book. Lorem Ipsum has been the industry's standard dummy text ever since the, when an unknown.</p>
</div>
<a class="abs pill-btn" href="#" style="left:191px;top:1892px;width:187px;height:44px">LEARN MORE
  <svg width="38" height="26" viewBox="0 0 38 26" fill="none" stroke="#111" stroke-width="1.3"><circle cx="25" cy="13" r="11"/><path d="M2 13h30M26 7l6 6-6 6"/></svg></a>

<!-- Who we are -->
<div class="abs ghost" style="left:517px;top:2185px">WHO WE</div>
<div class="photo" style="left:0;top:2410px;width:449px;height:287px;background:linear-gradient(180deg,#e8e9ea,#c9c9c6 55%,#8d8a84)" role="img" aria-label="Blue toy car on stacks of coins beside a glass jar"></div>
<div class="photo" style="left:313px;top:2286px;width:367px;height:170px;background:linear-gradient(90deg,#1f2a38,#7d8fa3 50%,#3c4654)" role="img" aria-label="Two business people shaking hands"></div>
<h2 class="abs sec-title" style="left:555px;top:2503px">WHO WE ARE</h2>
<div class="abs sec-copy" style="left:558px;top:2556px">
  <p>Lorem Ipsum has been the industry's standard dummy text ever since the 1500s, when an unknown printer took a galley of type &amp; scrambled it to make a type specimen book.</p>
  <p>Lorem Ipsum has been the industry's standard dummy text ever since the 1500s, when an unknown printer took a galley of type  scrambled it to make a type specimen book. Lorem Ipsum has been the industry's standard dummy text ever since the, when an unknown.</p>
</div>
<div class="abs rule" style="left:0;top:2787px;width:560px"></div>
<a class="abs pill-btn" href="#" style="left:558px;top:2765px;width:187px;height:45px">LEARN MORE
  <svg width="38" height="26" viewBox="0 0 38 26" fill="none" stroke="#111" stroke-width="1.3"><circle cx="25" cy="13" r="11"/><path d="M2 13h30M26 7l6 6-6 6"/></svg></a>

<!-- Contact -->
<div class="photo" style="left:275px;top:3090px;width:620px;height:320px;border-radius:120px 160px 80px 80px;background:radial-gradient(ellipse,#ececec 0,#f6f6f6 55%,rgba(255,255,255,0) 75%)" role="img" aria-label="Faint car shape made of banknotes"></div>
<h2 class="abs sec-title contact-head" style="top:2910px">CONTACT US</h2>
<p class="abs contact-head" style="top:2958px;font-size:15px;color:#444">Have an any Question for our services Contact Us Today!</p>
<div class="abs field" style="top:3024px;height:25px">Name *</div>
<div class="abs field" style="top:3073px;height:25px">Email *</div>
<div class="abs field" style="top:3122px;height:24px">Phone *</div>
<div class="abs field" style="top:3170px;height:102px">Message *</div>
<a class="abs pill-btn" href="#" style="left:525px;top:3297px;width:149px;height:43px">SUBMIT
  <svg width="38" height="26" viewBox="0 0 38 26" fill="none" stroke="#111" stroke-width="1.3"><circle cx="25" cy="13" r="11"/><path d="M2 13h30M26 7l6 6-6 6"/></svg></a>

<!-- Footer -->
<svg class="abs" style="left:0;top:3390px" width="1200" height="345" viewBox="0 0 1200 345"><polygon points="0,60 1200,0 1200,345 0,345" fill="#000"/></svg>
<div class="abs brand" style="left:60px;top:3481px;color:var(--white)">KELVA Finance</div>
<div class="abs foot-info" style="left:60px;top:3550px;display:flex;gap:12px">
  <svg width="16" height="24" viewBox="0 0 16 24" fill="none" stroke="#fff" stroke-width="2"><path d="M8 22s6-7 6-13A6 6 0 0 0 2 9c0 6 6 13 6 13z"/><circle cx="8" cy="9" r="2.2"/></svg>
  <div style="font-size:11px;line-height:17px">KELVA | finance<br>Lorem ipsum simple text print type .</div>
</div>
<div class="abs foot-info" style="left:60px;top:3594px;display:flex;gap:14px;align-items:center">
  <svg width="18" height="18" viewBox="0 0 24 24" fill="#fff"><path d="M5 3h4l2 5-2.5 1.5a11 11 0 0 0 6 6L16 13l5 2v4a2 2 0 0 1-2 2A16 16 0 0 1 3 5a2 2 0 0 1 2-2z"/></svg>
  <span style="font-size:13px">123 4567 2210</span>
</div>
<div class="abs foot-info" style="left:60px;top:3628px;display:flex;gap:14px;align-items:center">
  <svg width="18" height="14" viewBox="0 0 18 14"><rect width="18" height="14" rx="1" fill="#fff"/><path d="M1 1l8 6 8-6" fill="none" stroke="#000" stroke-width="1.5"/></svg>
  <span style="font-size:11.5px">info@kelva.finance.com</span>
</div>
<div class="abs" style="left:364px;top:3478px;width:1px;height:205px;background:#444"></div>
<div class="abs footer-col" style="left:394px;top:3472px"><h4>Vehicle</h4><ul><li>Lorem Ipsum has been.</li><li>Lorem Ipsum has been.</li><li>Lorem Ipsum has been.</li><li>Lorem Ipsum has been.</li></ul></div>
<div class="abs footer-col" style="left:647px;top:3472px"><h4>Equipment</h4><ul><li>Lorem Ipsum has been.</li><li>Lorem Ipsum has been.</li><li>Lorem Ipsum has been.</li><li>Lorem Ipsum has been.</li></ul></div>
<div class="abs footer-col" style="left:898px;top:3472px"><h4>Who We Are</h4><ul><li>Lorem Ipsum has been.</li><li>Lorem Ipsum has been.</li><li>Lorem Ipsum has been.</li><li>Lorem Ipsum has been.</li></ul></div>
<div class="abs" style="left:60px;top:3686px;width:1080px;height:1px;background:#444"></div>
<p class="abs" style="left:0;width:1200px;top:3706px;text-align:center;font-size:10.5px;color:#ccc">©KELVA | Finance - 2022 All rights reserved.</p>

</body>
</html>
```